Where the Morning Went: A Season of Turning

The book size is 6x9. I am more interested in an illustrative design like the one I have posted below with a picture of my face and then having elements in the background of a barn, a cross and my little girls eyes peaking out from behind the scenery.
"Where the Morning Went… A Season of Turning" is a gripping memoir of resilience, faith, and courage. Marlene Kostrova’s journey pulls back the curtain on a ranch family fractured by addiction, abuse, and chaos, while revealing an extraordinary path to self-discovery and purpose.
Marlene, her older sister Bettina, and their three younger brothers grow up in a destabilizing environment where frequent moves and changing schools are routine. All the while, they navigate life in the shadow of their father’s addiction, schizophrenia, and violent outbursts. With dark secrets of sexual abuse and domestic violence lurking behind closed doors, the family seems trapped in a cycle of destruction.
Yet, Marlene’s spirit remains unbroken. Anchored by her unshakable belief that God is her true father and Jesus her brother, she clings to her faith and a guiding philosophy she calls “the next right move”—a quiet force that propels her forward, even as those around her fall victim to their demons. As her siblings descend into addiction, incarceration, and heartbreak, Marlene works to protect herself from the same fate while holding onto the family she cherishes.
Described by those who know her as possessing sophisticated grit, Marlene rises above her circumstances with a unique blend of resilience, conscientiousness, and inner grace. She is driven by her belief in “organic truth”—the truth you possess before you are even born—which, once discovered, has the power to set you free into becoming who you were met to be. This profound conviction, along with her commitment to “the next right move,” guides her through life’s darkest moments.
Armed with a PhD in Human Science and experience as a child abuse and neglect investigator, therapist, professor, business leader and coach, Marlene’s true triumph lies in something far deeper: surviving three near-death experiences and realizing that her purpose transcends personal, professional, and material achievements. Rather than pursuing happiness, she dedicates herself to uncovering meaning.
In this inspiring and candid memoir, she invites readers on a journey of becoming—one marked by faith, perseverance, and the courage to listen to the voice of organic truth within. Her story is a testament to the resilience of the human spirit and a beacon of hope for anyone navigating their own path to reclaim their sense of self, purpose, and freedom.

```html
<!DOCTYPE html>
<html lang="en">
<head>
<meta charset="UTF-8">
<title>Where the Morning Went – Book Cover</title>
<link href="https://fonts.googleapis.com/css2?family=Bodoni+Moda:ital,opsz,wght@0,6..96,400;0,6..96,500;1,6..96,400;1,6..96,500&family=Montserrat:wght@600&display=swap" rel="stylesheet">
<style>
  :root {
    --page: #ffffff;
    --ink: #0b0b0b;
    --accent-pink: #ee6fb4;
    --tagline: #ffffff;
    --wash-magenta: #ee4f9e;
    --wash-violet: #a86bd6;
    --wash-blue: #3f8fd9;
    --wash-sky: #8cc8e8;
    --wash-mist: #f4f7f9;
  }
  * { box-sizing: border-box; margin: 0; padding: 0; }
  html, body {
    width: 1200px;
    height: 1200px;
    overflow: hidden;
    background: var(--page);
  }
  .canvas {
    position: relative;
    width: 1200px;
    height: 1200px;
    background: var(--page);
  }
  .cover {
    position: absolute;
    left: 233px;
    top: 50px;
    width: 734px;
    height: 1100px;
    overflow: hidden;
  }
  .cover-art {
    position: absolute;
    inset: 0;
    background: linear-gradient(165deg,
      var(--wash-magenta) 0%,
      var(--wash-violet) 22%,
      var(--wash-blue) 45%,
      var(--wash-sky) 68%,
      var(--wash-mist) 92%);
  }
  .tagline {
    position: absolute;
    top: 52px;
    left: 0;
    right: 0;
    text-align: center;
    font-family: "Montserrat", sans-serif;
    font-weight: 600;
    font-size: 23px;
    letter-spacing: 0.32em;
    color: var(--tagline);
    text-transform: uppercase;
  }
  .title {
    position: absolute;
    right: 54px;
    top: 400px;
    text-align: right;
    font-family: "Bodoni Moda", serif;
    font-weight: 500;
    font-size: 104px;
    line-height: 101px;
    color: var(--ink);
    text-transform: uppercase;
  }
  .title-line { display: block; }
  .title-line--accent {
    color: var(--accent-pink);
    font-style: italic;
    font-weight: 400;
  }
  .author {
    position: absolute;
    right: 54px;
    top: 945px;
    text-align: right;
    font-family: "Bodoni Moda", serif;
    font-weight: 400;
    font-size: 50px;
    line-height: 62px;
    color: var(--ink);
    text-transform: uppercase;
  }
  .author-line { display: block; }
</style>
</head>
<body>
  <main class="canvas">
    <section class="cover">
      <div class="cover-art" role="img" aria-label="Watercolour portrait illustration of a woman's face in blue tones beneath a wash of magenta, violet and orange"></div>
      <p class="tagline">A Season of Turning</p>
      <h1 class="title">
        <span class="title-line">Where</span>
        <span class="title-line">The</span>
        <span class="title-line">Morning</span>
        <span class="title-line title-line--accent">Went</span>
      </h1>
      <p class="author">
        <span class="author-line">Marlene</span>
        <span class="author-line">Kostrova</span>
      </p>
    </section>
  </main>
</body>
</html>
```